Calloway Law - New Letterhead/Logo

Hello!
THE FIRM NAME IS NOW CALLOWAY LAW. We recently just changed our name and we are in need of a classy letterhead. Attached I have a logo we have included in the past, but we are willing to look at other alternatives as well. I will also attach our current letterhead with our old name, Calloway & Associates. We are willing to go without attorney names. Please help! Thanks
Updates
Project Deadline Extended Reason: Haven't found anything we love Added Tuesday, November 1, 2016

```html
<!DOCTYPE html>
<html lang="en">
<head>
<meta charset="utf-8">
<title>Calloway Law – Letterhead</title>
<link rel="stylesheet" href="https://fonts.googleapis.com/css2?family=Cormorant+Garamond:wght@500;600&display=swap">
<style>
  :root {
    --backdrop: #dcdcdc;
    --paper: #ffffff;
    --ink: #1a1a1a;
    --band: #000000;
    --band-ink: #ffffff;
    --rule: #333333;
  }
  * { margin: 0; padding: 0; box-sizing: border-box; }
  html, body { width: 1200px; height: 1200px; overflow: hidden; }
  body {
    position: relative;
    background: var(--backdrop);
    font-family: "Cormorant Garamond", Georgia, serif;
    color: var(--ink);
  }
  .stage {
    position: absolute; left: 0; top: 0;
    width: 1200px; height: 968px;
  }
  .letterhead {
    position: absolute; left: 262px; top: 40px;
    width: 680px; height: 880px;
    background: var(--paper);
    box-shadow: 0 6px 18px rgba(0,0,0,0.12);
  }
  .letterhead__rule {
    position: absolute; left: 168px; top: 40px; bottom: 40px;
    width: 1px; background: var(--rule);
  }
  .letterhead__mark {
    position: absolute; left: 36px; top: 40px; width: 116px;
    display: flex; align-items: center; gap: 8px;
  }
  .mark-square { width: 14px; height: 14px; background: var(--ink); flex: none; }
  .letterhead__name {
    font-weight: 600; font-size: 17px; line-height: 1.05; letter-spacing: 0.5px;
  }
  .letterhead__contact {
    position: absolute; left: 28px; bottom: 52px; width: 132px;
    font-weight: 500; font-size: 11px; line-height: 1.35;
  }
  .contact__firm { font-weight: 600; font-size: 15px; letter-spacing: 0.5px; }
  .contact__attorney {
    font-size: 7.5px; letter-spacing: 1px; text-transform: uppercase;
    border-top: 1px solid var(--ink); padding-top: 2px; margin-bottom: 8px;
  }
  .contact__block + .contact__block { margin-top: 10px; }

  .brand-band {
    position: absolute; left: 0; top: 968px;
    width: 1200px; height: 232px;
    background: var(--band); color: var(--band-ink);
  }
  .lockup-stacked {
    position: absolute; left: 30px; top: 44px; width: 170px;
    text-align: center;
  }
  .lockup-stacked .mark-square,
  .lockup-inline .mark-square { background: var(--band-ink); }
  .lockup-stacked .mark-square { width: 70px; height: 70px; margin: 0 auto 18px; }
  .lockup__name {
    font-weight: 600; font-size: 27px; line-height: 1; letter-spacing: 1px;
  }
  .lockup__attorney {
    font-weight: 500; font-size: 9px; letter-spacing: 1.2px; text-transform: uppercase;
    border-top: 1px solid var(--band-ink); margin-top: 6px; padding-top: 4px;
  }
  .lockup-inline {
    position: absolute; right: 66px; top: 60px;
    display: flex; align-items: center; gap: 22px;
  }
  .lockup-inline .mark-square { width: 100px; height: 100px; }
  .lockup-inline .lockup__name { font-size: 32px; }
</style>
</head>
<body>
  <section class="stage">
    <article class="letterhead">
      <div class="letterhead__mark">
        <span class="mark-square"></span>
        <span class="letterhead__name">CALLOWAY LAW</span>
      </div>
      <div class="letterhead__rule"></div>
      <address class="letterhead__contact" style="font-style:normal">
        <div class="contact__firm">CALLOWAY LAW</div>
        <div class="contact__attorney">Marcus T. Calloway, Esq.</div>
        <div class="contact__block">
          2180 Larkspur Avenue, Suite 400<br>
          Millbrook Village<br>
          Colorado 80000
        </div>
        <div class="contact__block">
          Phone (555) 014-2290<br>
          Fax (555) 014-2291<br>
          www.callowaylegal.net
        </div>
      </address>
    </article>
  </section>

  <footer class="brand-band">
    <div class="lockup-stacked">
      <div class="mark-square"></div>
      <div class="lockup__name">CALLOWAY<br>LAW</div>
      <div class="lockup__attorney">Marcus T. Calloway, Esq</div>
    </div>
    <div class="lockup-inline">
      <span class="mark-square"></span>
      <div>
        <div class="lockup__name">CALLOWAY LAW</div>
        <div class="lockup__attorney">Marcus T. Calloway, Esq</div>
      </div>
    </div>
  </footer>
</body>
</html>
```